WordPress design for BraxtonVell.com

*****
OVERVIEW
*****
BraxtonVell.com needs a fresh, clean, professional design that effectively illustrates its talent in a thoughtful, impressive, and impactful way.
Vell Architecture & Interiors (www.braxtonvell.com) is a well-established, prestigious, well-publicized New England USA architecture firm. Founded in 1996, the privately-held company specializes in high-end residential projects with a focus on classic New England style architecture.
Business contact information is as noted below:
Address:
Vell Architecture & Interiors
87 Orchard Terrace
Needham, MA 02817
Telephone:
617-555-0138
781-555-0274
Email:
info@braxtonvell.com
An excerpt from the current site describes the outfit with this:
"Our architecture and interior design practices are centered around the philosophy that successful living spaces combine a focus on richly articulated detail and an in-depth knowledge of quality construction techniques."
*****
DESIGN RESEARCH
*****
In reviewing design ideas, the following sites were appealing:
Good
- Marcus Thorne Architects (http://mtaarchitects-example.com/) - Simple and clean, but almost too simple.
Better
- Penrose Galt Architecture (http://www.penrosegalt-example.com/) - Direct portfolio access. Simple and clean.
Best
- Brimwell Architects (http://www.brimwellarchitects-example.com/) - Clean, simple, easy to navigate
- QRV Architecture & Interiors (http://www.qrv-architects-example.com/) - Excellent use of high-resolution media, transitions, and navigation.
Here is an example of what is NOT desired:
Tolland Pryce Architects (http://www.tollandpryce-example.com/) - Cluttered, tight landing page. Uncertain navigation.
*****
OTHER DETAILS
*****
The grey in the Vell Architecture & Interiors logo is hex 636363. The font is unknown.
Updates
Project Deadline Extended
Reason: Hello everyone,
Thank you for your continued patience with this project. As it turns out, a critical member of the decision making team on our client's end has been out of the office this week. She will be back next week and is ready to be fully engaged with this. That said, we are extending the contest for at least 5 days. Next week will be much more active.
Thank you for your understanding.
Glasswick Technology Services
Project Deadline Extended
Reason: Hello everyone,
The customer was on vacation and only returned Monday of this week. That said, we need to extend the deadline for 5 days to afford time for review and comment.
Thank you for your patience! The designs submitted thus far are fantastic!
Thanks again,
Project Deadline Extended
Reason: Hello,
With so many designs, the customer is taking longer than anticipated to review them. They are looking at them offline and will process a large batch of comments when ready.
That said, the contest is being extended again.
Thank you for your continued patience.
Project Deadline Extended
Reason: Hello,
Because there are 108 designs to review and comment on, this is taking much longer than anticipated. That said, the contest is being extended another 5 days to ensure the customer has the desired outcome.
Thank you,
Target Market(s)
- Would-be clients
- Landowners
- Construction firms and general contractors
- High-end residential component manufacturers
- Media outlets
- All others interested in high-end residential architecture and interior design
Industry/Entity Type
Architecture
Requirements
Must have
- - Lots of media capabilities, such as embedded video (via ClipStream is fine), project image gallery, sliders for various functions, and social media integrations
- - At least one large slider on the landing page is critical, as well as space for standard lead-in things, such as news/events, opportunities, project highlights, and the likes
- - A high-resolution project showcase - finished projects and works in progress - is critical
- - A place to highlight business partners with the potential for reciprocation
- Form capabilities for things like information requests and general contacts from the public
- - Design must be handed off in a logically-layered (for WordPress) PSD with any and all additional source files provided (e.g. Photoshop, Illustrator, fonts, etc)
Nice to have
- - The WordPress design should be capable of fitting into the very popular FernLayouts Trellis theme.

```html
<!DOCTYPE html>
<html lang="en">
<head>
<meta charset="utf-8">
<title>Vell Architecture &amp; Interiors</title>
<link href="https://fonts.googleapis.com/css2?family=Raleway:wght@300;400;600;700&family=Lora:ital,wght@1,400;1,700&display=swap" rel="stylesheet">
<style>
  :root {
    --page-bg: #efefef;
    --brand-grey: #636363;
    --sidebar-grey: #666666;
    --sidebar-line: #737373;
    --tile-white: #ffffff;
    --ink: #2b2b2b;
    --body-text: #6f6f6f;
    --rule: #bdbdbd;
    --footer-bg: #e9e9e9;
    --footer-text: #8a8a8a;
  }
  * { box-sizing: border-box; margin: 0; padding: 0; }
  html, body { width: 1200px; height: 1142px; overflow: hidden; }
  body {
    position: relative;
    background: var(--page-bg);
    font-family: "Raleway", sans-serif;
    color: var(--body-text);
  }

  /* ---------- tile grid ---------- */
  .tile-grid {
    position: absolute;
    left: 36px; top: 41px;
    display: grid;
    grid-template-columns: repeat(4, 237px);
    grid-template-rows: repeat(6, 158px);
    gap: 8px;
  }
  .tile { position: relative; overflow: hidden; }
  .photo { width: 100%; height: 100%; }

  .brand-tile { background: var(--brand-grey); color: #fff; }
  .brand-name {
    position: absolute; top: 22px; left: 0; right: 0; text-align: center;
    font-weight: 300; font-size: 31px; letter-spacing: 4px; color: #d9d9d9;
  }
  .brand-sub {
    position: absolute; top: 59px; left: 0; right: 0; text-align: center;
    font-weight: 300; font-size: 7.5px; letter-spacing: 2.2px; color: #d9d9d9;
  }
  .brand-links {
    position: absolute; right: 11px; bottom: 9px;
    font-size: 11px; font-weight: 600; color: #fff; word-spacing: 2px;
  }
  .brand-links span { margin: 0 6px; font-weight: 400; }

  .text-tile {
    background: var(--tile-white);
    padding: 30px 32px 0;
    display: flex; flex-direction: column;
  }
  .text-tile h2 {
    font-weight: 700; font-size: 19px; line-height: 24px;
    color: var(--ink); text-transform: uppercase; margin-bottom: 14px;
  }
  .text-tile p { font-size: 12.6px; line-height: 19px; font-weight: 400; }
  .text-tile p + p { margin-top: 10px; }
  .read-more {
    margin-top: auto; margin-bottom: 29px;
    border-top: 1px solid var(--rule); padding-top: 10px;
    font-size: 9.5px; font-weight: 700; color: var(--ink); letter-spacing: .3px;
    width: 174px;
  }
  .service-list { list-style: none; margin-top: 10px; }
  .service-list li {
    font-size: 12.6px; line-height: 19px; padding-left: 17px; position: relative;
  }
  .service-list li::before {
    content: ""; position: absolute; left: 6px; top: 7px;
    width: 5px; height: 5px; border: 1px solid var(--body-text); border-radius: 50%;
  }

  .portfolio-tile { color: #fff; }
  .portfolio-tile .photo {
    background:
      linear-gradient(180deg, rgba(0,0,0,0) 55%, rgba(30,18,10,.55) 100%),
      radial-gradient(ellipse at 60% 35%, #8a8a80 0%, #4a4a44 40%, #26231f 75%),
      #2a2520;
  }
  .portfolio-icon { position: absolute; left: 32px; top: 203px; }
  .portfolio-title {
    position: absolute; left: 32px; top: 262px;
    font-size: 13.5px; font-weight: 700; letter-spacing: .1px;
  }
  .portfolio-year {
    position: absolute; left: 32px; top: 282px;
    font-family: "Lora", serif; font-style: italic; font-size: 10px;
  }
  .portfolio-arrow { position: absolute; right: 32px; top: 286px; }

  .quote-tile { background: var(--tile-white); padding: 30px 32px 0; }
  .quote-mark {
    position: absolute; right: 38px; bottom: -38px;
    font-family: "Lora", serif; font-size: 130px; line-height: 1; color: #f1f1f1;
  }
  .quote-text {
    position: relative;
    font-family: "Lora", serif; font-style: italic; font-size: 12.6px; line-height: 19px;
    color: var(--ink);
  }
  .quote-text strong { font-weight: 700; }
  .quote-author {
    position: absolute; right: 32px; top: 134px;
    font-size: 9.5px; color: var(--body-text);
  }

  /* ---------- sidebar ---------- */
  .sidebar {
    position: absolute; left: 1042px; top: 0; width: 158px; height: 1142px;
    background: var(--sidebar-grey); color: #fff;
  }
  .social-row { display: flex; gap: 9px; padding: 19px 0 0 30px; height: 47px; border-bottom: 1px solid var(--sidebar-line); }
  .social-dot { width: 8px; height: 8px; border-radius: 50%; background: #fff; }
  .main-nav { list-style: none; }
  .main-nav li {
    border-bottom: 1px solid var(--sidebar-line);
    padding: 0 8px 0 24px;
    display: flex; align-items: center;
    font-size: 9.8px; font-weight: 700; line-height: 10px; text-transform: uppercase;
  }
  .nav-short { height: 39.5px; }
  .nav-tall { height: 49.5px; }
  .copyright {
    position: absolute; left: 24px; top: 1096px;
    font-size: 9.8px; line-height: 14px;
  }

  /* ---------- footer ---------- */
  .site-footer {
    position: absolute; left: 0; top: 1070px; width: 1042px; height: 72px;
    background: var(--footer-bg); border-top: 1px solid #dddddd;
    display: flex; align-items: center; justify-content: center; gap: 5px;
    font-size: 9.4px; font-weight: 600; color: var(--footer-text); text-transform: uppercase;
  }
  .site-footer svg { vertical-align: -1px; }
</style>
</head>
<body>

<main class="tile-grid">
  <section class="tile brand-tile" style="grid-column:1;grid-row:1">
    <div class="brand-name">VELL</div>
    <div class="brand-sub">ARCHITECTURE &amp; INTERIORS</div>
    <nav class="brand-links">HOME<span>|</span>CONTACT</nav>
  </section>

  <div class="tile" style="grid-column:2/4;grid-row:1/3">
    <div class="photo" role="img" aria-label="Curving modern building beside classic apartment facades under a cloudy sky" style="background:linear-gradient(180deg,#b9c2c8 0%,#cfd3d2 40%,#d8d4c8 70%,#8c8a78 100%)"></div>
  </div>

  <section class="tile text-tile" style="grid-column:4;grid-row:1/3">
    <h2>Renovations<br>and Additions</h2>
    <p>At vero eos et accusamus et iusto odio dignissimos ducimus qui blanditiis praesentium voluptatum deleniti atque corrupti quos dolores et quas molestias excepturi sint</p>
    <div class="read-more">READ MORE</div>
  </section>

  <div class="tile" style="grid-column:1;grid-row:2">
    <div class="photo" role="img" aria-label="Stone-clad city corner building with rooftop terraces" style="background:linear-gradient(180deg,#a7acb0 0%,#cfc6b4 50%,#b9ab92 80%,#6d655a 100%)"></div>
  </div>

  <div class="tile" style="grid-column:1;grid-row:3">
    <div class="photo" role="img" aria-label="White modern house entrance with a wooden path and planted gravel beds" style="background:linear-gradient(180deg,#6f8fc7 0%,#c9d5e6 40%,#eeeeea 65%,#a49a88 85%,#5a5a58 100%)"></div>
  </div>

  <section class="tile text-tile" style="grid-column:2;grid-row:3/5">
    <h2>Architecture</h2>
    <p>At vero eos et accusamus et iusto odioo</p>
    <ul class="service-list">
      <li>Residential Construction</li>
      <li>Public Housing</li>
      <li>Commercial Building</li>
      <li>Industrial Facility</li>
      <li>Restoration</li>
    </ul>
    <div class="read-more">READ MORE</div>
  </section>

  <div class="tile" style="grid-column:3;grid-row:3">
    <div class="photo" role="img" aria-label="Sculptural curved steel facade panels against a pale sky" style="background:linear-gradient(135deg,#d6d8d8 0%,#9e9a92 45%,#6a655c 70%,#b8b4aa 100%)"></div>
  </div>

  <div class="tile" style="grid-column:4;grid-row:3">
    <div class="photo" role="img" aria-label="Angular zinc-clad museum beside a historic building and a lawn" style="background:linear-gradient(180deg,#8fa0b0 0%,#a8b4bc 40%,#7b8a92 58%,#6d8a3e 78%,#7a7468 100%)"></div>
  </div>

  <section class="tile text-tile" style="grid-column:1;grid-row:4/6">
    <h2>Design Interior</h2>
    <p>At vero eos et accusamus et iusto odio dignissimos ducimus qui blanditiis praesentium voluptatum deleniti atque corrupti quos dolores et quas molestias excepturi sint .</p>
    <p>At vero eos et accusamus et iusto odio dignissimos ducimus</p>
    <div class="read-more">READ MORE</div>
  </section>

  <section class="tile portfolio-tile" style="grid-column:3/5;grid-row:4/6">
    <div class="photo" role="img" aria-label="Interior with a sweeping white spiral staircase over a dark wooden floor"></div>
    <svg class="portfolio-icon" width="38" height="40" viewBox="0 0 38 40" fill="none" stroke="#fff" stroke-width="2" aria-hidden="true">
      <path d="M9 3h20v10c0 6-4.5 11-10 11S9 19 9 13z"/>
      <path d="M9 6H3c0 7 3 11 7 12M29 6h6c0 7-3 11-7 12"/>
      <path d="M19 24v6M12 37h14l-2-7H14z"/>
      <path d="M19 8l1.5 3 3.2.4-2.4 2.2.7 3.2-3-1.6-3 1.6.7-3.2-2.4-2.2 3.2-.4z" stroke-width="1.2"/>
    </svg>
    <div class="portfolio-title">INTERIOR DESIGN PORTFOLIO</div>
    <div class="portfolio-year">2015</div>
    <svg class="portfolio-arrow" width="18" height="8" viewBox="0 0 18 8" fill="none" stroke="#fff" stroke-width="1.2" aria-hidden="true">
      <path d="M0 4h17M13 1l4 3-4 3"/>
    </svg>
  </section>

  <div class="tile" style="grid-column:2;grid-row:5">
    <div class="photo" role="img" aria-label="Bright white kitchen island with tall windows and dark stools" style="background:linear-gradient(180deg,#cfd3d3 0%,#e8e8e6 45%,#f2f2f0 70%,#8a847c 100%)"></div>
  </div>

  <div class="tile" style="grid-column:1;grid-row:6">
    <div class="photo" role="img" aria-label="Warm kitchen with dark wood cabinets and a stone dining counter" style="background:linear-gradient(180deg,#ddd2c0 0%,#b8a890 40%,#6b4f3c 70%,#4a3a30 100%)"></div>
  </div>

  <div class="tile" style="grid-column:2;grid-row:6">
    <div class="photo" role="img" aria-label="Concrete terrace with wooden dining set overlooking green hills" style="background:linear-gradient(180deg,#d6d8d4 0%,#9aa58a 45%,#7c786c 70%,#3e3630 100%)"></div>
  </div>

  <section class="tile quote-tile" style="grid-column:3;grid-row:6">
    <div class="quote-mark" aria-hidden="true">&#8221;</div>
    <p class="quote-text">At vero eos et accusamus <strong>dignissimos ducimus</strong>, praesentium voluptatum deleniti atque corrupti quos dolores.</p>
    <div class="quote-author">— John Doe, Founder</div>
  </section>

  <div class="tile" style="grid-column:4;grid-row:6">
    <div class="photo" role="img" aria-label="Cream living room with white sofas and large windows onto a valley view" style="background:linear-gradient(180deg,#e4dccd 0%,#d9cfbd 45%,#c8b9a2 75%,#b7a58c 100%)"></div>
  </div>
</main>

<aside class="sidebar">
  <div class="social-row" aria-label="Social links">
    <span class="social-dot"></span><span class="social-dot"></span><span class="social-dot"></span><span class="social-dot"></span>
  </div>
  <ul class="main-nav">
    <li class="nav-short">About</li>
    <li class="nav-short">Architecture</li>
    <li class="nav-short">Interior Design</li>
    <li class="nav-short">Works in Progress</li>
    <li class="nav-tall">Renovations and<br>Additions</li>
    <li class="nav-tall">Publications and<br>Awards</li>
    <li class="nav-short">Affiliates</li>
  </ul>
  <div class="copyright">© 2015,<br>BraxtonVell.com</div>
</aside>

<footer class="site-footer">
  <svg width="7" height="9" viewBox="0 0 7 9" aria-hidden="true"><path d="M3.5 0A3.5 3.5 0 0 0 0 3.5C0 6 3.5 9 3.5 9S7 6 7 3.5A3.5 3.5 0 0 0 3.5 0zm0 5A1.5 1.5 0 1 1 3.5 2a1.5 1.5 0 0 1 0 3z" fill="#8a8a8a"/></svg>
  <span>87 Orchard Terrace Needham, MA 02817</span>
  <svg width="9" height="9" viewBox="0 0 9 9" aria-hidden="true"><path d="M2 0l1.6 2.2-1 1.2a5 5 0 0 0 3 3l1.2-1L9 7l-.8 1.6C4.3 9 0 4.7.4.8z" fill="#8a8a8a"/></svg>
  <span>617.555.0138</span>
  <svg width="10" height="8" viewBox="0 0 10 8" aria-hidden="true"><rect width="10" height="8" rx="1" fill="#8a8a8a"/><path d="M0.5 1l4.5 3.3L9.5 1" stroke="#e9e9e9" fill="none"/></svg>
  <span>info@braxtonvell.com</span>
</footer>

</body>
</html>
```